Add words, element to an already make product design

Hi guys,
I m already have the design (attached) which is a wet tissue product. The front main side (about 14cm x 7 cm) is the waves and the brand name Zelfo. However, in this main side, it should contain more words, which are "Khan uot" (mean wet wipe), and the words "Mat lanh" (mean cooling) and "Tinh khiet" (mean purity). "Khan uot" to indicate function of the product, while Mat lanh and Tinh khiet are just marketing term to add.
So yes, the task is quite simple, but I think the key is to choose an appropriate font, color and the location you decide where it should be. You can add any element you want, as long as it look good overall, and those words above, are required to have. More in the attached are few rival from our market, as some example.
Thank you, and wait your idea.

Hi guys, Just to tell you that the main front design will not change. So the waves and the brand name still keep the same. Just adding more words or elements to it. Thank you guys.

```html
<!DOCTYPE html>
<html lang="vi">
<head>
<meta charset="utf-8">
<title>Zelfo – Khăn ướt dieline</title>
<link rel="stylesheet" href="https://fonts.googleapis.com/css2?family=Open+Sans:wght@400;600;700;800&family=Baloo+2:wght@700&display=swap">
<style>
  :root {
    --paper: #ffffff;
    --ink: #111111;
    --dash: #222222;
    --brand-blue: #1b9ad6;
    --brand-light: #5bbde8;
    --wave-pale: #e2f3fb;
    --wave-mid: #43aee2;
    --wave-deep: #0b6fb6;
    --icon-blue: #1f86c6;
  }
  html, body {
    margin: 0;
    padding: 0;
    width: 1200px;
    height: 1200px;
    overflow: hidden;
    background: var(--paper);
  }
  .dieline { display: block; }
  .cut-line { fill: none; stroke: var(--dash); stroke-width: 1.6; stroke-dasharray: 14 8; }
  .measure { font-family: "Open Sans", Arial, sans-serif; fill: var(--ink); font-size: 34px; }
  .measure-large { font-size: 38px; }
  .info-text { font-family: "Open Sans", Arial, sans-serif; fill: var(--icon-blue); font-size: 11px; }
  .info-strong { font-weight: 600; }
  .disposal-text { font-family: "Open Sans", Arial, sans-serif; fill: var(--icon-blue); font-size: 7.5px; font-weight: 700; }
  .care-icon { fill: var(--paper); stroke: var(--icon-blue); stroke-width: 2; }
  .care-mark { fill: var(--icon-blue); }
  .test-badge { fill: var(--icon-blue); }
  .product-type { font-family: "Baloo 2", "Open Sans", sans-serif; font-weight: 700; font-size: 44px; fill: var(--paper); stroke: var(--brand-light); stroke-width: 2.4; paint-order: stroke; letter-spacing: 1px; }
  .brand-name { font-family: "Open Sans", Arial, sans-serif; font-weight: 800; font-size: 128px; fill: var(--brand-blue); letter-spacing: 2px; }
  .claim { font-family: "Open Sans", Arial, sans-serif; font-weight: 700; font-size: 31px; fill: var(--paper); letter-spacing: 4px; }
  .label-window { fill: var(--paper); }
  .batch-tab { fill: var(--brand-blue); }
  .batch-text { font-family: "Open Sans", Arial, sans-serif; font-size: 11px; fill: var(--ink); }
</style>
</head>
<body>
<svg class="dieline" width="1200" height="1200" viewBox="0 0 1200 1200" xmlns="http://www.w3.org/2000/svg">
  <defs>
    <linearGradient id="wave-tone" x1="0" y1="0" x2="0" y2="1">
      <stop offset="0" stop-color="var(--wave-pale)"/>
      <stop offset="0.28" stop-color="#a9dbf2"/>
      <stop offset="0.5" stop-color="var(--wave-mid)"/>
      <stop offset="1" stop-color="var(--wave-deep)"/>
    </linearGradient>
    <path id="claim-curve" d="M255 690 Q 470 780 745 725"/>
  </defs>

  <!-- front panel wave artwork -->
  <path role="img" aria-label="Watercolour blue waves, pale at the top deepening to dark blue"
        fill="url(#wave-tone)"
        d="M213 525 C 330 560, 420 640, 560 600 C 700 555, 800 540, 900 560 C 960 572, 990 585, 1010 580 L1010 1016 L213 1016 Z"/>

  <!-- label window -->
  <rect class="label-window" x="750" y="849" width="225" height="88"/>

  <!-- front panel text -->
  <text class="product-type" x="616" y="551" text-anchor="middle">Khăn ướt</text>
  <text class="brand-name" x="610" y="665" text-anchor="middle">Zelfo</text>

  <!-- snowflake -->
  <g transform="translate(268 685)" stroke="var(--paper)" stroke-width="3.5" stroke-linecap="round">
    <line x1="-16" y1="0" x2="16" y2="0"/>
    <line x1="-8" y1="-14" x2="8" y2="14"/>
    <line x1="-8" y1="14" x2="8" y2="-14"/>
  </g>
  <text class="claim"><textPath href="#claim-curve" startOffset="6%">Mat lanh</textPath></text>
  <!-- water drop -->
  <path fill="var(--paper)" d="M499 741 C 494 752, 491 756, 491 760 A 8 8 0 0 0 507 760 C 507 756, 504 752, 499 741 Z"/>
  <text class="claim"><textPath href="#claim-curve" startOffset="55%">Tinh khiet</textPath></text>

  <!-- top panel info -->
  <text class="info-text info-strong" x="478" y="252">NSX: 2 năm trước HSD</text>
  <text class="info-text" x="478" y="265">HSD: In trên bao bì</text>

  <g transform="rotate(180 324 287)">
    <text class="disposal-text" x="292" y="284">XIN BỎ VÀO ĐÚNG</text>
    <text class="disposal-text" x="300" y="294">NƠI QUY ĐỊNH</text>
  </g>

  <g class="care-icons">
    <rect class="care-icon" x="307" y="306" width="32" height="32" rx="4"/>
    <rect class="care-mark" x="315" y="314" width="16" height="16" rx="2"/>
    <rect class="care-icon" x="371" y="270" width="33" height="33" rx="4"/>
    <rect class="care-icon" x="413" y="270" width="33" height="33" rx="4"/>
    <circle class="care-mark" cx="429.5" cy="286.5" r="9"/>
    <rect class="care-icon" x="455" y="270" width="33" height="33" rx="4"/>
    <path class="care-mark" d="M462 295 L480 277 L483 280 L466 298 Z"/>
    <rect class="care-icon" x="371" y="312" width="33" height="33" rx="4"/>
    <rect class="care-mark" x="378" y="325" width="19" height="6" rx="2"/>
    <rect class="care-icon" x="413" y="312" width="33" height="33" rx="4"/>
    <circle class="care-mark" cx="429.5" cy="328.5" r="9"/>
    <rect class="care-icon" x="455" y="312" width="33" height="33" rx="4"/>
    <rect class="care-mark" x="461" y="323" width="21" height="10" rx="4"/>
    <path class="care-mark" d="M383 290 L393 278 L396 281 L386 293 Z"/>
  </g>

  <!-- test certificate badge -->
  <path class="test-badge" d="M858 262 L944 262 L952 280 L952 328 Q 930 350 902 350 Q 874 350 852 328 L852 280 Z"/>

  <!-- batch tab -->
  <rect class="batch-tab" x="139" y="1030" width="29" height="59"/>
  <text class="batch-text" transform="translate(142 1034) rotate(90)">BH</text>

  <!-- dieline -->
  <rect class="cut-line" x="139" y="116" width="945" height="973"/>
  <line class="cut-line" x1="213" y1="116" x2="213" y2="1089"/>
  <line class="cut-line" x1="1010" y1="116" x2="1010" y2="1089"/>
  <line class="cut-line" x1="139" y1="189" x2="1084" y2="189"/>
  <line class="cut-line" x1="139" y1="396" x2="1084" y2="396"/>
  <line class="cut-line" x1="139" y1="809" x2="1084" y2="809"/>
  <line class="cut-line" x1="139" y1="1016" x2="1084" y2="1016"/>

  <!-- measurements -->
  <text class="measure" x="184" y="101" text-anchor="middle">12.5</text>
  <text class="measure measure-large" x="610" y="101" text-anchor="middle">135</text>
  <text class="measure" x="1047" y="101" text-anchor="middle">12.5</text>
  <text class="measure measure-large" x="608" y="1143" text-anchor="middle">160 mm</text>
  <text class="measure" transform="translate(128 605) rotate(-90)" text-anchor="middle">165mm</text>
  <text class="measure" transform="translate(1104 140) rotate(90)" text-anchor="middle" style="font-size:26px">12.5</text>
  <text class="measure" transform="translate(1104 265) rotate(90)" text-anchor="middle" style="font-size:26px">35</text>
  <text class="measure" transform="translate(1104 572) rotate(90)" text-anchor="middle" style="font-size:26px">70</text>
  <text class="measure" transform="translate(1104 885) rotate(90)" text-anchor="middle" style="font-size:26px">35</text>
  <text class="measure" transform="translate(1104 1058) rotate(90)" text-anchor="middle" style="font-size:26px">12.5</text>
</svg>
</body>
</html>
```